Design a menu for a Pizza company

I need help designing a color menu for a pizza company. It will be a 9x16" trifold menu (3-panel). I would like to include some photos of pizza, salads, subs, sandwiches, drinks, etc. (no clipart). Attached is an example of an existing menu. I need to make the menu full color. We would like to modernize this menu with full color photos like the attached sample menu. The final files should have editable files so I can edit prices and menu items as needed. I prefer CorelDraw graphics software.

Target Market(s)

General public.

Industry/Entity Type

Restaurant

Font styles to use
Sans Serif

Colors
ec1f27
fffefc
9bcb3b

Requirements
Must have
• Must have photos and editable fonts. I will need to be able to edit the contents of the menu after you provide me with the final files.
Nice to have
• It would be nice to have this menu created in CorelDraw X7 or X8.
Should not have
• Should not have clip art or low resolution photos.

```html
<!DOCTYPE html>
<html lang="en">
<head>
<meta charset="utf-8">
<title>Pizza Restaurant Trifold Menu</title>
<link href="https://fonts.googleapis.com/css2?family=Arimo:wght@400;700&family=Oranienbaum&display=swap" rel="stylesheet">
<style>
:root{
  --red:#ec1f27;
  --paper:#fffefc;
  --green:#9bcb3b;
  --ink:#1d1d1d;
  --muted:#8a8a80;
  --stage:#2f3122;
}
*{margin:0;padding:0;box-sizing:border-box}
html,body{width:1200px;height:1200px;overflow:hidden;background:var(--stage)}
body{position:relative;font-family:"Arimo",Arial,sans-serif;color:var(--ink)}
.spread{position:absolute;left:193px;width:881px;height:495px;background:var(--paper);overflow:hidden;box-shadow:0 6px 14px rgba(0,0,0,.45)}
.spread.front{top:94px}
.spread.back{top:644px}
.section{position:absolute}
.section h2{font-family:"Oranienbaum",Georgia,serif;font-weight:400;color:var(--red);font-size:15px;letter-spacing:.3px;text-transform:uppercase;line-height:1}
.section h2 small{font-size:7px;color:var(--muted);letter-spacing:.2px}
.note{font-family:"Oranienbaum",Georgia,serif;color:var(--muted);font-size:6.4px;line-height:8px;text-transform:uppercase;margin-top:4px;width:165px}
.items{list-style:none}
.items li{display:flex;align-items:baseline;font-size:6.2px;line-height:11.5px;white-space:nowrap}
.items li b{font-size:8.5px;margin-right:3px}
.items li i{flex:1;border-bottom:1px dotted #777;margin:0 2px;transform:translateY(-2px)}
.items li em{font-style:normal;font-weight:700;font-size:8.5px}
.sub{color:var(--green);font-weight:700;font-size:9.5px;text-align:center;line-height:12px}
.photo{position:absolute;border-radius:50%}
.p-pasta{background:radial-gradient(circle,#f1e3b8,#d9c48b 60%,#e9e6dd)}
.p-seafood{background:radial-gradient(circle,#d9562c,#8f3a22 55%,#e8e2d6)}
.p-chicken{background:radial-gradient(circle,#d59a45,#b9772e 60%,#f3ead6)}
.p-drinks{border-radius:6px;background:linear-gradient(90deg,#e7c44a,#a01b24 30%,#7cc04a 60%,#e45a3a)}
.p-tea{border-radius:6px;background:linear-gradient(#9fc45a,#e08a3a)}
.p-beer{border-radius:6px;background:linear-gradient(90deg,#7a4a1e,#e2b233)}
.p-bowl{background:radial-gradient(ellipse,rgba(235,214,150,.35),rgba(255,254,252,0) 70%)}
.p-onion{background:radial-gradient(circle,#c8324f,#7e1e3c 60%,#f1e8ea)}
.p-fries{background:radial-gradient(ellipse,#f2c14b,#e6a82a 55%,rgba(255,254,252,0) 72%)}
.p-salad{background:radial-gradient(circle,#7fbf3a,#3f8a2a 60%,#eef2e6)}
.p-sub{border-radius:40%;background:linear-gradient(#d79a50,#b4392b 45%,#6fae3c 60%,#c98b45)}
.p-pizza-sm{background:radial-gradient(ellipse,#c4402a,#e3a156 55%,rgba(255,254,252,0) 72%)}
.p-burger{background:radial-gradient(circle,#d89a4a,#8a3a2a 55%,#f0e6d6)}
.divider{position:absolute;top:30px;bottom:30px;width:0;border-left:1px dotted #b8b8b0}
.cover{position:absolute;left:594px;top:0;width:287px;height:495px}
.cover .hero{position:absolute;left:0;top:0;width:287px;height:342px;background:linear-gradient(#f4f2ea 0,#f4f2ea 45%,#d98a3a 62%,#b8321f 80%,#5a3a22 100%)}
.cover .band{position:absolute;left:0;top:342px;width:287px;height:153px;background:var(--red)}
.brand{position:absolute;left:36px;top:49px;display:flex;align-items:center;gap:8px}
.brand .mark{width:64px;height:72px;background:var(--green)}
.brand .name{font-family:"Arimo",Arial,sans-serif;font-weight:400;color:var(--red);font-size:24px;line-height:26px;letter-spacing:.5px}
.tag{position:absolute;left:39px;width:82px;height:16px;color:#fff;font-size:11px;line-height:16px;text-align:center}
.tag.delivery{top:134px;background:var(--red)}
.tag.carry{top:154px;background:var(--green)}
.open-badge{position:absolute;left:70px;top:314px;width:147px;height:63px}
.open-badge span{position:absolute;left:0;width:100%;text-align:center;font-weight:700}
.hours{position:absolute;left:0;top:394px;width:287px;text-align:center;color:#fff;font-size:10.3px;line-height:14.5px}
.cards{position:absolute;left:77px;top:452px;width:133px;border-top:1px solid #f4a9ab;border-bottom:1px solid #f4a9ab;color:#fff;font-size:8.5px;line-height:16px;text-align:center}
</style>
</head>
<body>

<!-- FRONT SPREAD -->
<section class="spread front">
  <div class="photo p-bowl" role="img" aria-label="Faded plate of spaghetti in the background" style="left:330px;top:380px;width:240px;height:130px"></div>

  <div class="section" style="left:28px;top:33px;width:251px">
    <h2>Italian Dinners</h2>
    <p class="note">Served on garlic bread &amp; salad choice of dressing: ranch, french italian, blue cheese, thousand island</p>
  </div>
  <div class="photo p-pasta" role="img" aria-label="Plate of pasta with chicken" style="left:195px;top:18px;width:84px;height:56px"></div>
  <ul class="items section" style="left:28px;top:82px;width:251px">
    <li><b>French Fries</b> Served W/ Marinara Sauce<i></i><em>2.49</em></li>
    <li><b>Chicken Tenders</b> Served W/ Honey Mustard Sauce<i></i><em>6.49</em></li>
    <li><b>Jalapeno Peppers</b> Served W/Marinara Sauce<i></i><em>6.49</em></li>
    <li><b>8 Piece Buffalo Wings</b> Served W/ Blue Cheese Sauce<i></i><em>6.99</em></li>
    <li><b>Fried Mushroom</b> Served W/ Ranch Dressing<i></i><em>6.49</em></li>
    <li><b>French Fries</b> Served W/ Marinara Sauce<i></i><em>2.49</em></li>
    <li><b>Chicken Tenders</b> Served W/ Honey Mustard Sauce<i></i><em>6.49</em></li>
  </ul>

  <div class="section" style="left:28px;top:187px;width:251px">
    <h2>Seafood Dinners</h2>
    <p class="note">Served on garlic bread &amp; salad choice of dressing: ranch, french italian, blue cheese, tousand island</p>
  </div>
  <div class="photo p-seafood" role="img" aria-label="Plate of seafood pasta" style="left:197px;top:173px;width:82px;height:56px"></div>
  <ul class="items section" style="left:28px;top:237px;width:251px">
    <li><b>Mozzarella Sticks</b> Served W/ Marinara Sauce<i></i><em>6.49</em></li>
    <li><b>Chicken Tenders</b> Served W/ Honey Mustard Sauce<i></i><em>6.49</em></li>
    <li><b>Jalapeno Peppers</b> Served W/Marinara Sauce<i></i><em>6.49</em></li>
    <li><b>8 Piece Buffalo Wings</b> Served W/ Blue Cheese Sauce<i></i><em>6.99</em></li>
    <li><b>Fried Mushroom</b> Served W/ Ranch Dressing<i></i><em>6.49</em></li>
    <li><b>Jalapeno Peppers</b> Served W/Marinara Sauce<i></i><em>6.49</em></li>
    <li><b>8 Piece Buffalo Wings</b> Served W/ Blue Cheese Sauce<i></i><em>6.99</em></li>
    <li><b>Fried Mushroom</b> Served W/ Ranch Dressing<i></i><em>6.49</em></li>
  </ul>

  <div class="section" style="left:28px;top:354px"><h2>Children's Menu</h2></div>
  <div class="photo p-chicken" role="img" aria-label="Fried chicken pieces" style="left:205px;top:336px;width:70px;height:48px"></div>
  <ul class="items section" style="left:28px;top:368px;width:251px">
    <li><b>Mozzarella Sticks</b> Served W/ Marinara Sauce<i></i><em>6.49</em></li>
    <li><b>Chicken Tenders</b> Served W/ Honey Mustard Sauce<i></i><em>6.49</em></li>
    <li><b>Jalapeno Peppers</b> Served W/Marinara Sauce<i></i><em>6.49</em></li>
    <li><b>8 Piece Buffalo Wings</b> Served W/ Blue Cheese Sauce<i></i><em>6.99</em></li>
    <li><b>Fried Mushroom</b> Served W/ Ranch Dressing<i></i><em>6.49</em></li>
  </ul>

  <div class="divider" style="left:294px"></div>

  <div class="section" style="left:310px;top:33px"><h2>Soda</h2></div>
  <div class="photo p-drinks" role="img" aria-label="Four glasses of soda" style="left:455px;top:10px;width:86px;height:44px"></div>
  <ul class="items section" style="left:310px;top:51px;width:252px">
    <li><b>French Fries</b> Served W/ Marinara Sauce<i></i><em>2.49</em></li>
    <li><b>Chicken Tenders</b> Served W/ Honey Mustard Sauce<i></i><em>6.49</em></li>
    <li><b>Jalapeno Peppers</b> Served W/Marinara Sauce<i></i><em>6.49</em></li>
    <li><b>8 Piece Buffalo Wings</b> Served W/ Blue Cheese Sauce<i></i><em>6.99</em></li>
    <li><b>Fried Mushroom</b> Served W/ Ranch Dressing<i></i><em>6.49</em></li>
  </ul>

  <div class="section" style="left:311px;top:139px"><h2>Beverages</h2></div>
  <div class="photo p-tea" role="img" aria-label="Glass of iced tea with mint" style="left:490px;top:113px;width:30px;height:46px"></div>
  <ul class="items section" style="left:311px;top:157px;width:251px">
    <li><b>French Fries</b> Served W/ Marinara Sauce<i></i><em>2.49</em></li>
  </ul>

  <div class="section" style="left:310px;top:201px"><h2>Beer</h2></div>
  <div class="photo p-beer" role="img" aria-label="Two beer bottles" style="left:499px;top:201px;width:42px;height:70px"></div>
  <div class="section" style="left:310px;top:217px;width:252px">
    <p class="sub" style="width:180px">DRAFT</p>
    <ul class="items" style="width:252px">
      <li><b>Mozzarella Sticks</b> Served W/ Marinara Sauce<i></i><em>6.49</em></li>
      <li><b>Chicken Tenders</b> Served W/ Honey Mustard Sauce<i></i><em>6.49</em></li>
      <li><b>Jalapeno Peppers</b> Served W/Marinara Sauce<i></i><em>6.49</em></li>
    </ul>
    <p class="sub" style="width:252px;margin-top:7px">BOTTLES</p>
    <ul class="items" style="width:252px">
      <li><b>Mozzarella Sticks</b> Served W/ Marinara Sauce<i></i><em>6.49</em></li>
      <li><b>Chicken Tenders</b> Served W/ Honey Mustard Sauce<i></i><em>6.49</em></li>
      <li><b>Jalapeno Peppers</b> Served W/Marinara Sauce<i></i><em>6.49</em></li>
      <li><b>8 Piece Buffalo Wings</b> Served W/ Blue Cheese Sauce<i></i><em>6.99</em></li>
      <li><b>Fried Mushroom</b> Served W/ Ranch Dressing<i></i><em>6.49</em></li>
    </ul>
    <p class="sub" style="width:252px;margin-top:7px">IMPORTED BOTTLES</p>
    <ul class="items" style="width:252px">
      <li><b>Mozzarella Sticks</b> Served W/ Marinara Sauce<i></i><em>6.49</em></li>
      <li><b>Chicken Tenders</b> Served W/ Honey Mustard Sauce<i></i><em>6.49</em></li>
    </ul>
  </div>

  <div class="cover">
    <div class="hero" role="img" aria-label="Pizza with a slice being lifted and melted cheese stretching"></div>
    <div class="brand">
      <div class="mark"></div>
      <div class="name">PIZZA<br>RESTAURANT</div>
    </div>
    <div class="tag delivery">DELIVERY</div>
    <div class="tag carry">CARRY-OUT</div>
    <div class="band"></div>
    <div class="open-badge">
      <svg width="147" height="63" viewBox="0 0 147 63" aria-hidden="true">
        <polygon points="73.5,0 147,63 0,63" fill="#9bcb3b"/>
        <circle cx="16" cy="57" r="2" fill="#1d1d1d"/>
        <circle cx="131" cy="57" r="2" fill="#1d1d1d"/>
      </svg>
      <span style="top:30px;font-size:19px;color:var(--red);line-height:20px">OPEN</span>
      <span style="top:50px;font-size:9.5px;line-height:11px">7 DAYS A WEEK</span>
    </div>
    <p class="hours">Monday - Thursday 10:30 A.M. - 9:30 P.M.<br>Friday &amp; Saturday 10:30 A.M. - 10:00 P.M.<br>Sunday 12:00 Noon - 8:00 P.M.</p>
    <p class="cards">Major Credit Cards Accepted</p>
  </div>
</section>

<!-- BACK SPREAD -->
<section class="spread back">
  <div class="section" style="left:28px;top:34px"><h2>Appetizers</h2></div>
  <div class="photo p-onion" role="img" aria-label="Appetizer with red onion" style="left:210px;top:18px;width:50px;height:42px"></div>
  <ul class="items section" style="left:28px;top:53px;width:251px">
    <li><b>Mozzarella Sticks</b> Served W/ Marinara Sauce<i></i><em>6.49</em></li>
    <li><b>Chicken Tenders</b> Served W/ Honey Mustard Sauce<i></i><em>6.49</em></li>
    <li><b>Jalapeno Peppers</b> Served W/Marinara Sauce<i></i><em>6.49</em></li>
    <li><b>8 Piece Buffalo Wings</b> Served W/ Blue Cheese Sauce<i></i><em>6.99</em></li>
    <li><b>Fried Mushroom</b> Served W/ Ranch Dressing<i></i><em>6.49</em></li>
  </ul>

  <div class="section" style="left:28px;top:147px"><h2>Side Orders</h2></div>
  <div class="photo p-fries" role="img" aria-label="Pile of french fries" style="left:170px;top:124px;width:110px;height:50px"></div>
  <ul class="items section" style="left:28px;top:167px;width:251px">
    <li><b>French Fries</b> Served W/ Marinara Sauce<i></i><em>2.49</em></li>
    <li><b>Chicken Tenders</b> Served W/ Honey Mustard Sauce<i></i><em>6.49</em></li>
    <li><b>Jalapeno Peppers</b> Served W/Marinara Sauce<i></i><em>6.49</em></li>
    <li><b>8 Piece Buffalo Wings</b> Served W/ Blue Cheese Sauce<i></i><em>6.99</em></li>
    <li><b>Fried Mushroom</b> Served W/ Ranch Dressing<i></i><em>6.49</em></li>
  </ul>

  <div class="section" style="left:28px;top:261px"><h2>Garden Fresh Salds</h2></div>
  <div class="photo p-salad" role="img" aria-label="Bowl of fresh garden salad" style="left:190px;top:238px;width:82px;height:50px"></div>
  <ul class="items section" style="left:28px;top:281px;width:251px">
    <li><b>Mozzarella Sticks</b> Served W/ Marinara Sauce<i></i><em>6.49</em></li>
    <li><b>Chicken Tenders</b> Served W/ Honey Mustard Sauce<i></i><em>6.49</em></li>
    <li><b>Jalapeno Peppers</b> Served W/Marinara Sauce<i></i><em>6.49</em></li>
    <li><b>8 Piece Buffalo Wings</b> Served W/ Blue Cheese Sauce<i></i><em>6.99</em></li>
    <li><b>Fried Mushroom</b> Served W/ Ranch Dressing<i></i><em>6.49</em></li>
  </ul>

  <div class="section" style="left:28px;top:375px"><h2>Sandwiches</h2></div>
  <div class="photo p-sub" role="img" aria-label="Long submarine sandwich" style="left:165px;top:362px;width:110px;height:32px"></div>
  <ul class="items section" style="left:28px;top:395px;width:251px">
    <li><b>Mozzarella Sticks</b> Served W/ Marinara Sauce<i></i><em>6.49</em></li>
    <li><b>Chicken Tenders</b> Served W/ Honey Mustard Sauce<i></i><em>6.49</em></li>
    <li><b>Jalapeno Peppers</b> Served W/Marinara Sauce<i></i><em>6.49</em></li>
    <li><b>8 Piece Buffalo Wings</b> Served W/ Blue Cheese Sauce<i></i><em>6.99</em></li>
    <li><b>Fried Mushroom</b> Served W/ Ranch Dressing<i></i><em>6.49</em></li>
  </ul>

  <div class="divider" style="left:294px"></div>

  <div class="section" style="left:314px;top:34px"><h2>Super Subs <small>served cold</small></h2></div>
  <div class="photo p-sub" role="img" aria-label="Cold sub sandwich" style="left:485px;top:18px;width:62px;height:38px"></div>
  <ul class="items section" style="left:314px;top:51px;width:251px">
    <li><b>Mozzarella Sticks</b> Served W/ Marinara Sauce<i></i><em>6.49</em></li>
    <li><b>Chicken Tenders</b> Served W/ Honey Mustard Sauce<i></i><em>6.49</em></li>
    <li><b>Jalapeno Peppers</b> Served W/Marinara Sauce<i></i><em>6.49</em></li>
    <li><b>8 Piece Buffalo Wings</b> Served W/ Blue Cheese Sauce<i></i><em>6.99</em></li>
    <li><b>Fried Mushroom</b> Served W/ Ranch Dressing<i></i><em>6.49</em></li>
    <li><b>Jalapeno Peppers</b> Served W/Marinara Sauce<i></i><em>6.49</em></li>
    <li><b>8 Piece Buffalo Wings</b> Served W/ Blue Cheese Sauce<i></i><em>6.99</em></li>
    <li><b>Fried Mushroom</b> Served W/ Ranch Dressing<i></i><em>6.49</em></li>
  </ul>

  <div class="section" style="left:314px;top:175px"><h2>Hot Subs</h2></div>
  <div class="photo p-sub" role="img" aria-label="Hot sub sandwich" style="left:468px;top:152px;width:78px;height:44px"></div>
  <ul class="items section" style="left:314px;top:190px;width:251px">
    <li><b>French Fries</b> Served W/ Marinara Sauce<i></i><em>2.49</em></li>
    <li><b>Chicken Tenders</b> Served W/ Honey Mustard Sauce<i></i><em>6.49</em></li>
    <li><b>Jalapeno Peppers</b> Served W/Marinara Sauce<i></i><em>6.49</em></li>
    <li><b>8 Piece Buffalo Wings</b> Served W/ Blue Cheese Sauce<i></i><em>6.99</em></li>
    <li><b>Fried Mushroom</b> Served W/ Ranch Dressing<i></i><em>6.49</em></li>
    <li><b>French Fries</b> Served W/ Marinara Sauce<i></i><em>2.49</em></li>
    <li><b>Chicken Tenders</b> Served W/ Honey Mustard Sauce<i></i><em>6.49</em></li>
    <li><b>Jalapeno Peppers</b> Served W/Marinara Sauce<i></i><em>6.49</em></li>
    <li><b>8 Piece Buffalo Wings</b> Served W/ Blue Cheese Sauce<i></i><em>6.99</em></li>
    <li><b>Fried Mushroom</b> Served W/ Ranch Dressing<i></i><em>6.49</em></li>
    <li><b>French Fries</b> Served W/ Marinara Sauce<i></i><em>2.49</em></li>
    <li><b>Chicken Tenders</b> Served W/ Honey Mustard Sauce<i></i><em>6.49</em></li>
    <li><b>Jalapeno Peppers</b> Served W/Marinara Sauce<i></i><em>6.49</em></li>
    <li><b>8 Piece Buffalo Wings</b> Served W/ Blue Cheese Sauce<i></i><em>6.99</em></li>
  </ul>

  <div class="section" style="left:314px;top:380px"><h2>Parmigiana Subs</h2></div>
  <div class="photo p-sub" role="img" aria-label="Parmigiana sub sandwich" style="left:480px;top:358px;width:70px;height:40px"></div>
  <ul class="items section" style="left:314px;top:395px;width:251px">
    <li><b>Mozzarella Sticks</b> Served W/ Marinara Sauce<i></i><em>6.49</em></li>
    <li><b>Chicken Tenders</b> Served W/ Honey Mustard Sauce<i></i><em>6.49</em></li>
    <li><b>Jalapeno Peppers</b> Served W/Marinara Sauce<i></i><em>6.49</em></li>
    <li><b>8 Piece Buffalo Wings</b> Served W/ Blue Cheese Sauce<i></i><em>6.99</em></li>
    <li><b>Fried Mushroom</b> Served W/ Ranch Dressing<i></i><em>6.49</em></li>
  </ul>

  <div class="divider" style="left:578px"></div>

  <div class="section" style="left:595px;top:34px"><h2>Pizza</h2></div>
  <div class="photo p-pizza-sm" role="img" aria-label="Whole pizza" style="left:740px;top:14px;width:112px;height:42px"></div>
  <ul class="items section" style="left:595px;top:51px;width:252px">
    <li><b>French Fries</b> Served W/ Marinara Sauce<i></i><em>2.49</em></li>
    <li><b>Chicken Tenders</b> Served W/ Honey Mustard Sauce<i></i><em>6.49</em></li>
    <li><b>Jalapeno Peppers</b> Served W/Marinara Sauce<i></i><em>6.49</em></li>
    <li><b>8 Piece Buffalo Wings</b> Served W/ Blue Cheese Sauce<i></i><em>6.99</em></li>
    <li><b>Fried Mushroom</b> Served W/ Ranch Dressing<i></i><em>6.49</em></li>
    <li><b>French Fries</b> Served W/ Marinara Sauce<i></i><em>2.49</em></li>
    <li><b>Chicken Tenders</b> Served W/ Honey Mustard Sauce<i></i><em>6.49</em></li>
    <li><b>Jalapeno Peppers</b> Served W/Marinara Sauce<i></i><em>6.49</em></li>
    <li><b>8 Piece Buffalo Wings</b> Served W/ Blue Cheese Sauce<i></i><em>6.99</em></li>
    <li><b>Fried Mushroom</b> Served W/ Ranch Dressing<i></i><em>6.49</em></li>
    <li><b>French Fries</b> Served W/ Marinara Sauce<i></i><em>2.49</em></li>
    <li><b>Chicken Tenders</b> Served W/ Honey Mustard Sauce<i></i><em>6.49</em></li>
    <li><b>Jalapeno Peppers</b> Served W/Marinara Sauce<i></i><em>6.49</em></li>
    <li><b>8 Piece Buffalo Wings</b> Served W/ Blue Cheese Sauce<i></i><em>6.99</em></li>
  </ul>

  <div class="section" style="left:595px;top:237px"><h2>Sandwich Platters</h2></div>
  <div class="photo p-burger" role="img" aria-label="Roast beef sandwich" style="left:768px;top:214px;width:60px;height:46px"></div>
  <ul class="items section" style="left:595px;top:254px;width:252px">
    <li><b>Mozzarella Sticks</b> Served W/ Marinara Sauce<i></i><em>6.49</em></li>
    <li><b>Chicken Tenders</b> Served W/ Honey Mustard Sauce<i></i><em>6.49</em></li>
    <li><b>Jalapeno Peppers</b> Served W/Marinara Sauce<i></i><em>6.49</em></li>
    <li><b>8 Piece Buffalo Wings</b> Served W/ Blue Cheese Sauce<i></i><em>6.99</em></li>
    <li><b>Fried Mushroom</b> Served W/ Ranch Dressing<i></i><em>6.49</em></li>
    <li><b>Jalapeno Peppers</b> Served W/Marinara Sauce<i></i><em>6.49</em></li>
    <li><b>8 Piece Buffalo Wings</b> Served W/ Blue Cheese Sauce<i></i><em>6.99</em></li>
    <li><b>Fried Mushroom</b> Served W/ Ranch Dressing<i></i><em>6.49</em></li>
  </ul>

  <div class="section" style="left:595px;top:381px"><h2>Sandwiches <small>served on sesame bun</small></h2></div>
  <div class="photo p-burger" role="img" aria-label="Burger on a sesame bun" style="left:778px;top:350px;width:62px;height:50px"></div>
  <ul class="items section" style="left:595px;top:396px;width:252px">
    <li><b>Mozzarella Sticks</b> Served W/ Marinara Sauce<i></i><em>6.49</em></li>
    <li><b>Chicken Tenders</b> Served W/ Honey Mustard Sauce<i></i><em>6.49</em></li>
    <li><b>Jalapeno Peppers</b> Served W/Marinara Sauce<i></i><em>6.49</em></li>
    <li><b>8 Piece Buffalo Wings</b> Served W/ Blue Cheese Sauce<i></i><em>6.99</em></li>
    <li><b>Fried Mushroom</b> Served W/ Ranch Dressing<i></i><em>6.49</em></li>
  </ul>
</section>

</body>
</html>
```